Marlow Bay Kestrel Arrivals Flyer

A 2 sided DL size flyer. (Approx 20cm long by 10cm wide)
That has logo and blurb about company on front. On back details of Kestrel arrivals package, trademark, contact details and license numbers.
We feel we need to see the text on the flyer design and then make some changes so there will be some back and forth about written content. There may be a reduction in the amount of text we want for the blurb about the company but the rest is mandatory.
Our logo is blue and green, we do not want a white flyer with black text as feel this looks homemade so we need your suggestions about what colour the text and flyer could be.
We want the flyer to look clean and modern. It will go on a stand at an immigration fair and will be sent in the post and via email to clients. We will need posters at a later stage.
Migrants
It Company

```html
<!DOCTYPE html>
<html lang="en">
<head>
<meta charset="utf-8">
<title>Marlow Bay Kestrel Arrivals Flyer</title>
<link href="https://fonts.googleapis.com/css2?family=Open+Sans:wght@400;600;700;800&display=swap" rel="stylesheet">
<style>
:root{
  --blue:#1f6fd1;
  --blue-deep:#1556b3;
  --green:#2fb344;
  --black:#111111;
  --white:#ffffff;
  --stage:#e9e9e9;
  --text-blue:#1f6fd1;
}
*{margin:0;padding:0;box-sizing:border-box}
html,body{width:733px;height:1200px;overflow:hidden}
body{background:var(--stage);font-family:"Open Sans",Arial,sans-serif;color:var(--white);position:relative}
.flyer{position:absolute;top:260px;width:340px;height:680px;background:var(--blue);overflow:hidden;box-shadow:0 4px 14px rgba(0,0,0,.25)}
.flyer--front{left:17px}
.flyer--back{left:376px}
.band{position:absolute;left:0;width:100%;overflow:hidden}
.header{top:0;height:85px;background:var(--white);display:flex;align-items:center;padding:0 18px;gap:12px}
.brand-dot{width:44px;height:44px;border-radius:50%;background:var(--green);flex:none}
.brand-name{font-weight:700;font-size:18px;line-height:1.1;color:var(--text-blue)}
.seal{margin-left:auto;width:62px;height:62px;border-radius:50%;background:#b8b79a;border:3px solid #8f8e74;flex:none}
.front-title{top:85px;height:70px;background:var(--blue-deep);padding:12px 16px 0;text-align:center;font-size:18px;line-height:1.2;letter-spacing:.2px}
.front-title strong{font-weight:800}
.front-title .lead{font-weight:400}
.photo{top:155px;height:152px;background:linear-gradient(180deg,#2a79cf 0%,#3f8fd8 45%,#8fbfe6 62%,#5b88b0 78%,#2d6fb4 100%)}
.green-head{top:307px;height:75px;background:var(--green);text-align:center;padding-top:12px;font-size:21px;line-height:1.05}
.green-head .thin{font-weight:400}
.green-head .heavy{font-weight:800}
.body-copy{top:382px;height:147px;background:var(--blue);text-align:center;padding:14px 18px 0;font-size:9.6px;line-height:1.36}
.body-copy p+p{margin-top:8px}
.quote{top:529px;height:52px;background:var(--green);text-align:center;padding:10px 18px 0;font-size:10px;font-weight:700;line-height:1.3}
.trained{top:581px;height:65px;background:var(--blue);text-align:center;padding:9px 24px 0;font-size:9.6px;line-height:1.33}
.footer-web{top:646px;height:34px;background:var(--black);display:flex;align-items:center;justify-content:center;gap:6px;font-size:15px;font-weight:600}
.footer-web svg{flex:none}
.back-title{top:85px;height:30px;background:var(--blue-deep);text-align:center;font-size:17px;font-weight:700;line-height:30px;letter-spacing:.2px}
.intro{top:115px;height:105px;background:var(--green);padding:9px 20px 0;font-size:9.6px;line-height:1.34}
.intro p+p{margin-top:10px}
.benefits{top:220px;height:198px;background:var(--blue)}
.benefits-backdrop{position:absolute;inset:0;background:linear-gradient(90deg,var(--blue) 0%,#2a7bd6 60%,#3384d8 80%,var(--blue) 100%)}
.benefit-list{position:relative;list-style:none;padding:14px 20px 0 20px}
.benefit-list li{display:flex;gap:9px;font-size:9.6px;line-height:1.3;margin-bottom:9px}
.benefit-list svg{flex:none;margin-top:1px}
.includes{top:418px;height:40px;background:var(--black);padding:5px 24px 0;font-size:11px;line-height:1.3;font-weight:600}
.includes strong{font-weight:700}
.options{top:458px;height:126px;background:var(--green);padding:10px 24px 0 28px;font-size:9.4px;line-height:1.3}
.options li{margin-bottom:9px;list-style:none}
.plan{top:584px;height:33px;background:var(--black);text-align:center;padding-top:4px;font-size:10.4px;line-height:1.3}
.plan strong{font-weight:700}
.contacts{top:617px;height:39px;background:var(--blue);display:flex;padding:5px 12px 0}
.contact{flex:1;font-size:9.4px;line-height:1.2}
.contact+.contact{border-left:2px solid var(--white);padding-left:8px}
.contact .who{font-size:13px;font-weight:700}
.footer-mail{top:656px;height:24px;background:var(--green);display:flex;align-items:center;justify-content:center;gap:6px;font-size:12px}
</style>
</head>
<body>

<section class="flyer flyer--front">
  <header class="band header">
    <span class="brand-dot"></span>
    <span class="brand-name">Marlow Bay Kestrel Arrivals</span>
  </header>
  <h1 class="band front-title"><span class="lead">FRIENDLY &amp; HELPFUL</span> <strong>LICENSED<br>IMMIGRATION ADVISERS</strong></h1>
  <div class="band photo" role="img" aria-label="Photograph of horse riders on a wet beach in front of tall sea rock arches under a blue sky"></div>
  <h2 class="band green-head"><span class="thin">WE FACILITATE FAST AND</span><br><span class="heavy">PROBLEM FREE VISAS</span></h2>
  <div class="band body-copy">
    <p>Marlow Bay Kestrel Arrivals is a family business; headed by two sisters – Ada and Ruth Fenwick. Originally from the UK they migrated to New Zealand over ten years ago, so understand how it feels to move to a new country &amp; go through the visa process.</p>
    <p>Ruth &amp; Ada are passionate about what New Zealand has to offer and enjoy the chance to help people make their home here. They work across all types of visa applications – to live, work or study.</p>
  </div>
  <blockquote class="band quote">“Working closely with you to meet your immigration goals, we help and guide you at every stage.”</blockquote>
  <p class="band trained">Trained and qualified, they have specialist knowledge of the immigration system. Able to work to urgent timeframes or with clients who have character or health issues.</p>
  <footer class="band footer-web">
    <svg width="16" height="16" viewBox="0 0 16 16" aria-hidden="true"><circle cx="8" cy="8" r="7" fill="none" stroke="var(--green)" stroke-width="1.5"/><path d="M1 8h14M8 1c3 3 3 11 0 14M8 1c-3 3-3 11 0 14" fill="none" stroke="var(--green)" stroke-width="1"/></svg>
    <span>www.kestrelarrivals.example</span>
  </footer>
</section>

<section class="flyer flyer--back">
  <header class="band header">
    <span class="brand-dot"></span>
    <span class="brand-name">Marlow Bay Kestrel Arrivals</span>
    <span class="seal" aria-hidden="true"></span>
  </header>
  <h2 class="band back-title">KESTREL ARRIVALS PACKAGE</h2>
  <div class="band intro">
    <p>Set yourself on a clear pathway from your first student visa to permanent residency with our comprehensive immigration package.</p>
    <p>Connect with licensed advisers who walk alongside you in your New Zealand journey, helping to make the most of your time and money</p>
  </div>
  <div class="band benefits">
    <div class="benefits-backdrop" role="img" aria-label="Faint photograph of a hot air balloon against a blue sky"></div>
    <ul class="benefit-list">
      <li><svg width="12" height="12" viewBox="0 0 12 12" aria-hidden="true"><circle cx="6" cy="6" r="5" fill="none" stroke="#fff" stroke-width="1.3"/><path d="M3.5 6.2l1.8 1.7 3.2-3.5" fill="none" stroke="#fff" stroke-width="1.3"/></svg><span>Confirmed, discounted rates for ongoing visas once your study is completed</span></li>
      <li><svg width="12" height="12" viewBox="0 0 12 12" aria-hidden="true"><circle cx="6" cy="6" r="5" fill="none" stroke="#fff" stroke-width="1.3"/><path d="M3.5 6.2l1.8 1.7 3.2-3.5" fill="none" stroke="#fff" stroke-width="1.3"/></svg><span>A one on one session with a licensed adviser to plan how to maximise your studies &amp; work opportunities to achieve residency faster</span></li>
      <li><svg width="12" height="12" viewBox="0 0 12 12" aria-hidden="true"><circle cx="6" cy="6" r="5" fill="none" stroke="#fff" stroke-width="1.3"/><path d="M3.5 6.2l1.8 1.7 3.2-3.5" fill="none" stroke="#fff" stroke-width="1.3"/></svg><span>Attendance at an immigration seminar</span></li>
      <li><svg width="12" height="12" viewBox="0 0 12 12" aria-hidden="true"><circle cx="6" cy="6" r="5" fill="none" stroke="#fff" stroke-width="1.3"/><path d="M3.5 6.2l1.8 1.7 3.2-3.5" fill="none" stroke="#fff" stroke-width="1.3"/></svg><span>Vital updates on immigration policy changes &amp; how they impact on you</span></li>
      <li><svg width="12" height="12" viewBox="0 0 12 12" aria-hidden="true"><circle cx="6" cy="6" r="5" fill="none" stroke="#fff" stroke-width="1.3"/><path d="M3.5 6.2l1.8 1.7 3.2-3.5" fill="none" stroke="#fff" stroke-width="1.3"/></svg><span>Access immediate advice from someone who knows your situation if things go wrong</span></li>
    </ul>
  </div>
  <div class="band includes">OUR KESTREL ARRIVALS PACKAGE INCLUDES 3<br><strong>VISA APPLICATIONS, CHOOSE FROM:</strong></div>
  <ol class="band options">
    <li>1. Deposit of 15% which covers Post Study Open Visa (job search)</li>
    <li>2. Either Post Study Employer Assisted Visa or Essential Skills Work Visa - (this includes employer support)</li>
    <li>3. Either Skilled Migrant Category Residence or Work to Residence Visa (both components for latter) Add on's for family and work options available.</li>
  </ol>
  <p class="band plan"><strong>Let Marlow Bay Kestrel Arrivals plan</strong><br>your route to residency.</p>
  <div class="band contacts">
    <div class="contact"><div class="who">Ruth-021 480 271</div>License Number -201388017</div>
    <div class="contact"><div class="who">Ada-021 093 47718</div>License Number 201645902</div>
  </div>
  <footer class="band footer-mail">
    <svg width="14" height="14" viewBox="0 0 14 14" aria-hidden="true"><circle cx="7" cy="7" r="6.3" fill="none" stroke="#fff" stroke-width="1.2"/><rect x="3.6" y="4.8" width="6.8" height="4.6" fill="none" stroke="#fff" stroke-width="1"/><path d="M3.6 4.8l3.4 2.6 3.4-2.6" fill="none" stroke="#fff" stroke-width="1"/></svg>
    <span>hello@kestrelarrivals.example</span>
  </footer>
</section>

</body>
</html>
```